BRL business card

For a business card with our logo

Contact Information for Business Card

Mathéo VRANEL
Founder & CEO
email : ceo@brightlanterncollective.com / www.brightlanterncollective.com /
instagram / facebook / WhatsApp
N°: +590 690 482 517

Colors

Designer to choose colors to be used in the design.

```html
<!DOCTYPE html>
<html lang="en">
<head>
<meta charset="utf-8">
<title>BRL business card</title>
<link rel="stylesheet" href="https://fonts.googleapis.com/css2?family=Lato:wght@400;700&display=swap">
<style>
  :root {
    --backdrop: #2a2a2c;
    --card-white: #f7f7f7;
    --brand-orange: #f2400c;
    --brand-orange-deep: #d93308;
    --brand-blue: #2a3fc4;
    --ink: #333333;
    --soft-line: #e4e4e4;
  }
  * { margin: 0; padding: 0; box-sizing: border-box; }
  html, body {
    width: 1200px;
    height: 997px;
    overflow: hidden;
    background: var(--backdrop);
    font-family: "Lato", sans-serif;
  }
  .stage {
    position: relative;
    width: 1200px;
    height: 997px;
  }
  .card {
    position: absolute;
    width: 520px;
    height: 298px;
    border-radius: 22px;
    overflow: hidden;
    box-shadow: 0 18px 40px rgba(0, 0, 0, 0.45);
  }
  .card-front {
    left: 50px;
    top: 350px;
    background: var(--card-white);
  }
  .card-back {
    left: 630px;
    top: 350px;
    background: linear-gradient(135deg, var(--brand-orange) 0%, var(--brand-orange-deep) 100%);
  }
  .card-shapes {
    position: absolute;
    inset: 0;
  }
  .brand-lockup {
    position: absolute;
    display: flex;
    align-items: center;
    gap: 10px;
  }
  .card-front .brand-lockup {
    left: 150px;
    top: 40px;
  }
  .brand-dot {
    width: 34px;
    height: 34px;
    border-radius: 50%;
    background: var(--brand-orange);
    flex: none;
  }
  .brand-name {
    font-weight: 700;
    font-size: 17px;
    letter-spacing: 0.06em;
    text-transform: uppercase;
    color: var(--brand-blue);
    line-height: 1.15;
  }
  .holder {
    position: absolute;
    left: 26px;
    top: 168px;
  }
  .holder-name {
    font-weight: 700;
    font-size: 19px;
    color: var(--brand-blue);
  }
  .holder-role {
    font-size: 14px;
    color: var(--brand-orange);
    margin-top: 2px;
  }
  .contact-list {
    position: absolute;
    left: 26px;
    top: 226px;
    list-style: none;
    font-size: 12px;
    color: var(--ink);
  }
  .contact-list li,
  .social-list li {
    display: flex;
    align-items: center;
    gap: 7px;
    height: 19px;
  }
  .contact-icon {
    width: 13px;
    height: 13px;
    flex: none;
  }
  .social-list {
    position: absolute;
    left: 338px;
    top: 196px;
    list-style: none;
    font-size: 11px;
    color: var(--ink);
  }
  .social-dot {
    width: 12px;
    height: 12px;
    border-radius: 50%;
    background: var(--brand-blue);
    flex: none;
  }
  .web-address {
    position: absolute;
    right: 20px;
    bottom: 16px;
    font-size: 12px;
    font-weight: 700;
    color: #ffffff;
  }
  .card-back .brand-lockup {
    left: 0;
    right: 0;
    top: 82px;
    flex-direction: column;
    gap: 16px;
  }
  .card-back .brand-dot {
    width: 86px;
    height: 86px;
    background: #f4f4f4;
  }
  .card-back .brand-name {
    color: #f4f4f4;
    font-size: 26px;
    letter-spacing: 0.08em;
    text-align: center;
  }
</style>
</head>
<body>
<main class="stage">

  <section class="card card-front" aria-label="Business card front">
    <svg class="card-shapes" width="520" height="298" viewBox="0 0 520 298" aria-hidden="true">
      <line x1="190" y1="0" x2="190" y2="150" stroke="var(--soft-line)" stroke-width="1"/>
      <line x1="330" y1="0" x2="330" y2="150" stroke="var(--soft-line)" stroke-width="1"/>
      <line x1="220" y1="178" x2="505" y2="150" stroke="var(--brand-orange)" stroke-width="1"/>
      <path d="M0 266 L290 266 L290 274 L0 274 Z" fill="var(--brand-blue)"/>
      <path d="M0 284 L300 284 Q318 284 320 266 L322 252 Q324 240 340 240 L520 240 L520 298 L0 298 Z" fill="var(--brand-orange)"/>
    </svg>

    <div class="brand-lockup">
      <span class="brand-dot"></span>
      <span class="brand-name">Bright Lantern<br>Collective</span>
    </div>

    <div class="holder">
      <p class="holder-name">Mathéo VRANEL</p>
      <p class="holder-role">Founder &amp; CEO</p>
    </div>

    <ul class="contact-list">
      <li>
        <svg class="contact-icon" viewBox="0 0 16 16" aria-hidden="true">
          <circle cx="8" cy="8" r="8" fill="var(--brand-orange)"/>
          <path d="M5 4.5 L6.6 4.5 L7.2 6.6 L6.3 7.3 Q7.2 9 8.7 9.8 L9.4 8.9 L11.5 9.5 L11.5 11.1 Q8 11.4 6 9.2 Q4.6 7.4 5 4.5 Z" fill="#fff"/>
        </svg>
        <span>+590 690 482 517</span>
      </li>
      <li>
        <svg class="contact-icon" viewBox="0 0 16 16" aria-hidden="true">
          <circle cx="8" cy="8" r="8" fill="var(--brand-orange)"/>
          <rect x="4" y="5.2" width="8" height="5.6" fill="none" stroke="#fff" stroke-width="1"/>
          <path d="M4 5.4 L8 8.4 L12 5.4" fill="none" stroke="#fff" stroke-width="1"/>
        </svg>
        <span>ceo@brightlanterncollective.com</span>
      </li>
    </ul>

    <ul class="social-list">
      <li><span class="social-dot"></span><span>brightlanterncollective</span></li>
      <li><span class="social-dot"></span><span>brightlanterncollective</span></li>
    </ul>

    <p class="web-address">www.brightlanterncollective.com</p>
  </section>

  <section class="card card-back" aria-label="Business card back">
    <div class="brand-lockup">
      <span class="brand-dot"></span>
      <span class="brand-name">Bright Lantern Collective</span>
    </div>
  </section>

</main>
</body>
</html>
```